UI design for kiosk touch screen

We need a UI design for a touch screen device to be used by costumers in a store and show information about specific products. We're looking for a general concept to serve as a starting point and we're not expecting a fully coded design.
We envision a UI where it first shows a range of products; once touched, it should show information about the product which includes text, touchable photos, videos and document files. We're interested in the starting page and the product details page.
We are the suppliers of the device and not the owners of stores that will use them. The purpose of this design is for in-person demonstrations to potential clients or in ads so the design should be agnostic about the end product(s). You may freely pick random placeholder or fictional products and assets to showcase the design concept as long as they can be changed without compromising the design. You can use our logo (annexed) in the design as a placeholder but it's not necessary.
We're using web technologies to develop the UI so the same principles should apply, except some exceptions below:
- There's no need for a responsive design since the resolution is set at 1920x1080 on a 22'' monitor in landscape orientation.
- All interactions will be done using the touchscreen, so any interactive component needs to be large enough for navigation to be comfortable.
- The design should be visually engaging and eye-catching, more so than a regular website.
Physical shop owners.
Store
2 page

```html
<!DOCTYPE html>
<html lang="en">
<head>
<meta charset="utf-8">
<title>Product Details – Circular Saw</title>
<link rel="stylesheet" href="https://fonts.googleapis.com/css2?family=Merriweather+Sans:wght@300;400;700;800&family=Noto+Sans:wght@300;400&family=Oswald:wght@700&display=swap">
<style>
  :root {
    --bg: #3a3a3a;
    --yellow: #f5c400;
    --orange: #f39c00;
    --badge: #ff8a00;
    --white: #ffffff;
    --title-grey: #9c9a8f;
    --text: #f0f0f0;
    --brand-blue: #2a8cff;
  }
  * { box-sizing: border-box; margin: 0; padding: 0; }
  html, body { width: 1200px; height: 675px; overflow: hidden; background: var(--bg); }
  .screen {
    position: relative; width: 1200px; height: 675px; background: var(--bg);
    font-family: "Merriweather Sans", sans-serif; color: var(--text);
  }
  .brand-name {
    position: absolute; left: 30px; top: 26px;
    font-family: "Oswald", sans-serif; font-weight: 700; font-size: 31px;
    color: var(--yellow); letter-spacing: 0.5px; line-height: 1;
  }
  .page-title {
    position: absolute; left: 0; width: 1178px; top: 26px; text-align: center;
    font-weight: 700; font-size: 31px; color: var(--title-grey);
  }
  .back-button {
    position: absolute; left: 31px; top: 86px; width: 106px; height: 37px;
    border: 1.5px solid var(--yellow); color: var(--yellow);
    display: flex; align-items: center; justify-content: center; gap: 8px;
    font-family: "Noto Sans", sans-serif; font-size: 16px;
  }
  .media-viewer { position: absolute; left: 30px; top: 163px; width: 535px; height: 413px; }
  .media-main {
    position: absolute; left: 0; top: 0; width: 535px; height: 300px;
    background: radial-gradient(ellipse at 55% 40%, #2c2622 0%, #1a1715 40%, #6d6a66 75%, #a9a6a1 100%);
  }
  .play-button { position: absolute; left: 249px; top: 102px; }
  .thumb-strip { position: absolute; left: 0; top: 300px; width: 535px; height: 113px; display: flex; }
  .thumb { width: 112px; height: 113px; flex: none; }
  .thumb-saw { background: linear-gradient(135deg, #f4f4f2 0%, #8d8d80 55%, #f7f7f5 100%); }
  .thumb-blade { background: linear-gradient(160deg, #4f4a44 0%, #9c9a94 45%, #3f5c9c 100%); }
  .thumb-edge { width: 87px; }
  .thumb-arrow { position: absolute; }
  .thumb-arrow.prev { left: 16px; }
  .thumb-arrow.next { right: 16px; }
  .product-heading {
    position: absolute; left: 581px; top: 155px; height: 46px;
    display: flex; align-items: center; gap: 11px;
  }
  .product-name {
    font-weight: 700; font-size: 36px; line-height: 1;
    color: var(--white); letter-spacing: -0.5px; white-space: nowrap;
  }
  .new-badge {
    flex: none; width: 44px; height: 44px; border-radius: 50%;
    background: var(--badge); color: var(--white); font-weight: 700; font-size: 14px;
    display: flex; align-items: center; justify-content: center;
  }
  .price {
    position: absolute; right: 60px; top: 154px; font-weight: 700; font-size: 39px; color: var(--yellow);
    white-space: nowrap;
  }
  .feature-list { position: absolute; top: 218px; list-style: none; }
  .feature-list.col-a { left: 583px; }
  .feature-list.col-b { left: 783px; top: 220px; }
  .feature-list li {
    display: flex; align-items: center; gap: 9px; height: 35px; white-space: nowrap;
    font-family: "Noto Sans", sans-serif; font-size: 21px; color: var(--white);
  }
  .description {
    position: absolute; left: 582px; top: 346px; width: 600px;
    font-family: "Noto Sans", sans-serif; font-weight: 300; font-size: 16px;
    line-height: 22.5px; letter-spacing: 0.7px; color: var(--text); white-space: nowrap;
  }
  .description p + p { margin-top: 22px; }
  .tech-heading {
    position: absolute; left: 582px; top: 503px; font-weight: 700; font-size: 15.5px; color: var(--white);
  }
  .document-list { position: absolute; left: 581px; top: 538px; display: flex; gap: 13px; }
  .document-button {
    width: 150px; height: 37px; border: 1.5px solid var(--yellow);
    display: flex; align-items: center; justify-content: center; gap: 9px;
    font-weight: 300; font-size: 15px; color: var(--yellow); white-space: nowrap;
  }
  .vendor-name {
    position: absolute; right: 30px; top: 617px; display: flex; align-items: center; gap: 6px;
    font-weight: 800; font-size: 17px; color: var(--brand-blue);
  }
  .vendor-name .mark { width: 16px; height: 16px; background: var(--orange); }
</style>
</head>
<body>
<main class="screen">
  <div class="brand-name">TOOLNEST</div>
  <h1 class="page-title">Product Details</h1>
  <a class="back-button">
    <svg width="10" height="16" viewBox="0 0 10 16"><path d="M8 1 L2 8 L8 15" fill="none" stroke="currentColor" stroke-width="1.5"/></svg>
    Back
  </a>

  <section class="media-viewer">
    <div class="media-main" role="img" aria-label="Video still of a circular saw blade cutting metal with sparks flying"></div>
    <svg class="play-button" width="98" height="98" viewBox="0 0 98 98">
      <circle cx="49" cy="49" r="46" fill="none" stroke="var(--orange)" stroke-width="4"/>
      <path d="M39 29 L67 49 L39 69 Z" fill="none" stroke="var(--orange)" stroke-width="4" stroke-linejoin="round"/>
    </svg>
    <div class="thumb-strip">
      <div class="thumb thumb-saw" role="img" aria-label="Product photo of the circular saw"></div>
      <div class="thumb thumb-blade" role="img" aria-label="Photo of the saw cutting a board"></div>
      <div class="thumb thumb-saw" role="img" aria-label="Product photo of the circular saw"></div>
      <div class="thumb thumb-blade" role="img" aria-label="Photo of the saw cutting a board"></div>
      <div class="thumb thumb-saw thumb-edge" role="img" aria-label="Product photo of the circular saw"></div>
    </div>
    <svg class="thumb-arrow prev" width="20" height="36" viewBox="0 0 20 36" style="top:338px"><path d="M17 2 L3 18 L17 34" fill="none" stroke="var(--yellow)" stroke-width="3"/></svg>
    <svg class="thumb-arrow next" width="20" height="36" viewBox="0 0 20 36" style="top:338px"><path d="M3 2 L17 18 L3 34" fill="none" stroke="var(--yellow)" stroke-width="3"/></svg>
  </section>

  <div class="product-heading">
    <h2 class="product-name">Circular Saw</h2>
    <span class="new-badge">new</span>
  </div>
  <div class="price">$ 655</div>

  <ul class="feature-list col-a">
    <li><svg width="17" height="17" viewBox="0 0 17 17"><rect x="1" y="3" width="13" height="13" fill="none" stroke="var(--yellow)" stroke-width="1.6"/><path d="M4 9 L7.5 12 L16 2" fill="none" stroke="var(--yellow)" stroke-width="1.8"/></svg>Ultra durable</li>
    <li><svg width="17" height="17" viewBox="0 0 17 17"><rect x="1" y="3" width="13" height="13" fill="none" stroke="var(--yellow)" stroke-width="1.6"/><path d="M4 9 L7.5 12 L16 2" fill="none" stroke="var(--yellow)" stroke-width="1.8"/></svg>Easy to use</li>
    <li><svg width="17" height="17" viewBox="0 0 17 17"><rect x="1" y="3" width="13" height="13" fill="none" stroke="var(--yellow)" stroke-width="1.6"/><path d="M4 9 L7.5 12 L16 2" fill="none" stroke="var(--yellow)" stroke-width="1.8"/></svg>New design</li>
  </ul>
  <ul class="feature-list col-b">
    <li><svg width="17" height="17" viewBox="0 0 17 17"><rect x="1" y="3" width="13" height="13" fill="none" stroke="var(--yellow)" stroke-width="1.6"/><path d="M4 9 L7.5 12 L16 2" fill="none" stroke="var(--yellow)" stroke-width="1.8"/></svg>Extended warrenty</li>
    <li><svg width="17" height="17" viewBox="0 0 17 17"><rect x="1" y="3" width="13" height="13" fill="none" stroke="var(--yellow)" stroke-width="1.6"/><path d="M4 9 L7.5 12 L16 2" fill="none" stroke="var(--yellow)" stroke-width="1.8"/></svg>12 AMPs</li>
    <li><svg width="17" height="17" viewBox="0 0 17 17"><rect x="1" y="3" width="13" height="13" fill="none" stroke="var(--yellow)" stroke-width="1.6"/><path d="M4 9 L7.5 12 L16 2" fill="none" stroke="var(--yellow)" stroke-width="1.8"/></svg>Free 2 blades</li>
  </ul>

  <div class="description">
    <p>Lorem ipsum dolor sit amet, consectetur adipisicing elit, sed do eiusmod<br>tempor incididunt ut labore et dolore magna aliqua.</p>
    <p>Ut enim ad minim veniam, quis nostrud exercitation ullamco laboris nisi<br>ut aliquip ex ea commodo consequat. Duis aute irure dolor in<br>reprehenderit in voluptate velit esse cillum dolore eu fugiat nulla</p>
  </div>

  <h3 class="tech-heading">Technical information</h3>
  <div class="document-list">
    <a class="document-button">Specifications
      <svg width="20" height="24" viewBox="0 0 20 24"><path d="M1 1 H13 L19 7 V23 H1 Z M13 1 V7 H19" fill="none" stroke="var(--yellow)" stroke-width="1.5"/><rect x="3" y="13" width="11" height="6" fill="var(--yellow)"/></svg></a>
    <a class="document-button">Specifications
      <svg width="20" height="24" viewBox="0 0 20 24"><path d="M1 1 H13 L19 7 V23 H1 Z M13 1 V7 H19" fill="none" stroke="var(--yellow)" stroke-width="1.5"/><rect x="3" y="13" width="11" height="6" fill="var(--yellow)"/></svg></a>
    <a class="document-button">Specifications
      <svg width="20" height="24" viewBox="0 0 20 24"><path d="M1 1 H13 L19 7 V23 H1 Z M13 1 V7 H19" fill="none" stroke="var(--yellow)" stroke-width="1.5"/><rect x="3" y="13" width="11" height="6" fill="var(--yellow)"/></svg></a>
  </div>

  <div class="vendor-name"><span class="mark"></span>KIOSKVIEW</div>
</main>
</body>
</html>
```